Business card to promote business guidance

I need a card design to give to all my customers advertising a way to build a business exactly like the one they just bought from. I have an online store and will include one with each shipment. It should state the way to financial freedom and working for yourself

Target Market(s)

Young Entrepreneurs that want to start and don't know how

Industry/Entity Type

Business

Contact Information for Business Card

"You just bought from a successful company on Brindlemart. I have a unique business model, discovered by me, unlike any other that can make anyone successful. Follow me and message me for exactly the same model. If you ever wanted to work for yourself, I will teach you how. It's not a pipe dream, allow me to guide you out of the box."

Colors
85abd2

Requirements
Must have
• website www.dorianwelkby.example
instagram @thedorianwelkby

```html
<!DOCTYPE html>
<html lang="en">
<head>
<meta charset="utf-8">
<title>Dorian Welkby — Business Card</title>
<link rel="stylesheet" href="https://fonts.googleapis.com/css2?family=Poppins:wght@400;500&family=Roboto+Condensed:ital,wght@0,300;1,300&display=swap">
<style>
  :root {
    --stage: #ffa200;
    --teal: #22a0bf;
    --navy: #032d45;
    --navy-cell: #05324c;
    --orange: #fb8500;
    --yellow: #ffb703;
    --white: #ffffff;
    --soft-white: #e6f4f8;
  }
  * { margin: 0; padding: 0; box-sizing: border-box; }
  html, body { width: 1200px; height: 800px; overflow: hidden; }
  body {
    background: var(--stage);
    font-family: "Roboto Condensed", "Arial Narrow", sans-serif;
    position: relative;
  }
  .card {
    position: absolute;
    top: 250px;
    width: 520px;
    height: 300px;
    background: var(--teal);
    overflow: hidden;
    box-shadow: 0 18px 40px rgba(0,0,0,0.25);
  }
  .card--front { left: 50px; }
  .card--back { left: 630px; }
  .card__decor { position: absolute; inset: 0; width: 100%; height: 100%; }

  /* Front */
  .brand {
    position: absolute;
    left: 48px;
    top: 82px;
    display: flex;
    align-items: center;
    gap: 12px;
    color: var(--white);
  }
  .brand__mark {
    width: 34px; height: 34px;
    border-radius: 50%;
    background: var(--white);
  }
  .brand__name {
    font-family: "Poppins", sans-serif;
    font-weight: 500;
    font-size: 30px;
    line-height: 1;
  }
  .brand__role {
    font-family: "Roboto Condensed", sans-serif;
    font-weight: 300;
    font-size: 13px;
    margin-top: 3px;
  }
  .contacts {
    position: absolute;
    left: 0; right: 0;
    top: 190px;
    height: 74px;
    display: flex;
    background: var(--navy);
  }
  .contact {
    flex: 1;
    display: flex;
    flex-direction: column;
    align-items: center;
    justify-content: center;
    gap: 8px;
    color: var(--white);
    font-family: "Poppins", sans-serif;
    font-size: 9.5px;
  }
  .contact + .contact { border-left: 2px solid var(--navy-cell); background: #042f47; }
  .contact__icon {
    width: 28px; height: 28px;
    border-radius: 50%;
    background: var(--orange);
    display: flex; align-items: center; justify-content: center;
  }

  /* Back */
  .message {
    position: absolute;
    left: 0; right: 0;
    top: 74px;
    text-align: center;
    color: var(--soft-white);
    font-style: italic;
    font-weight: 300;
    font-size: 14.5px;
    line-height: 1.5;
    padding: 0 40px;
  }
</style>
</head>
<body>

<section class="card card--front" aria-label="Business card front">
  <svg class="card__decor" viewBox="0 0 520 300" aria-hidden="true">
    <polygon points="300,0 345,0 385,40 345,40" fill="var(--yellow)"/>
    <polygon points="345,0 440,0 520,110 520,160 470,160 360,48 400,48" fill="var(--orange)"/>
    <polygon points="440,0 455,0 520,88 520,104" fill="var(--orange)"/>
    <polygon points="455,0 470,0 520,68 520,80" fill="var(--teal)"/>
    <polygon points="400,60 420,60 470,160 455,160" fill="var(--yellow)"/>
    <polygon points="0,130 60,190 0,190" fill="var(--yellow)"/>
    <polygon points="0,160 30,190 0,190" fill="var(--orange)"/>
  </svg>

  <div class="brand">
    <span class="brand__mark"></span>
    <div>
      <div class="brand__name">Dorian Welkby</div>
      <div class="brand__role">Business Consultan</div>
    </div>
  </div>

  <div class="contacts">
    <div class="contact">
      <span class="contact__icon"></span>
      <span>@thedorianwelkby</span>
    </div>
    <div class="contact">
      <span class="contact__icon">
        <svg width="16" height="12" viewBox="0 0 16 12" aria-hidden="true">
          <rect x="0.5" y="0.5" width="15" height="11" fill="var(--white)"/>
          <polyline points="0.5,0.5 8,7 15.5,0.5" fill="none" stroke="var(--orange)" stroke-width="1.4"/>
        </svg>
      </span>
      <span>thedorianwelkby@mail.example</span>
    </div>
    <div class="contact">
      <span class="contact__icon">
        <svg width="16" height="16" viewBox="0 0 16 16" aria-hidden="true" fill="none" stroke="var(--white)" stroke-width="1.1">
          <circle cx="8" cy="8" r="6.5"/>
          <ellipse cx="8" cy="8" rx="3" ry="6.5"/>
          <line x1="1.5" y1="8" x2="14.5" y2="8"/>
          <line x1="2.5" y1="4.5" x2="13.5" y2="4.5"/>
          <line x1="2.5" y1="11.5" x2="13.5" y2="11.5"/>
        </svg>
      </span>
      <span>www.dorianwelkby.example</span>
    </div>
  </div>
</section>

<section class="card card--back" aria-label="Business card back">
  <svg class="card__decor" viewBox="0 0 520 300" aria-hidden="true">
    <rect x="0" y="0" width="520" height="52" fill="var(--navy)"/>
    <rect x="175" y="0" width="2" height="52" fill="var(--navy-cell)"/>
    <rect x="350" y="0" width="2" height="52" fill="var(--navy-cell)"/>
    <rect x="0" y="250" width="520" height="50" fill="var(--navy)"/>
    <rect x="175" y="250" width="2" height="50" fill="var(--navy-cell)"/>
    <rect x="350" y="250" width="2" height="50" fill="var(--navy-cell)"/>
    <polygon points="370,250 520,178 520,206 410,250" fill="var(--orange)"/>
    <polygon points="470,190 520,166 520,176 480,196" fill="var(--yellow)"/>
    <polygon points="420,250 520,210 520,218 440,250" fill="var(--yellow)"/>
  </svg>

  <p class="message">
    “You just bought from a successful company on Brindlemart.<br>
    I have a unique business model, discovered by me,<br>
    unlike any other that can make anyone successful.<br>
    Follow me and message me for exactly the same model.<br>
    If you ever wanted to work for yourself, I will teach you how.<br>
    It's not a pipe dream, allow me to guide you out of the box.”
  </p>
</section>

</body>
</html>
```